Business Card and Letterhead Design for Public Accounting Firm

Business card and letterhead design for a CPA Firm located in Orange County, CA. We're looking for a modern and professional design utilizing our existing logo. We'd like a clean "less is more" look, but also something that catches the eye. We provide a high level of service to our clients. Open to single or double sided business cards.

Additional info: color numbers on logo
Blue :
R 0
G 83
B 125

#00537D

Silver :

R 154
G 154
B 154

#9A9A9A

Target Market(s)

Businesses and individuals

Industry/Entity Type

Accounting

Contact Information for Business Card

Moss Whitfield & Danby LLP - 4827 Larkspur Vale Road, Irvine, CA 92614 - (949)731-2864 - mwdaccts.example

Font styles to use
Serif
Sans Serif
Other font styles liked:
• See font file uploaded

Colors
0054AA
0677BA
7BADD7
CADEEF
E8F1F8

Requirements
Nice to have
• Possibly use the font file provided which matches our logo, but adjust to be not in all caps

```html
<!DOCTYPE html>
<html lang="en">
<head>
<meta charset="utf-8">
<title>Moss Whitfield &amp; Danby LLP — Business Card</title>
<link rel="stylesheet" href="https://fonts.googleapis.com/css2?family=Cinzel:wght@500&family=Noto+Serif:wght@400&display=swap">
<style>
  :root {
    --backdrop: #2b2b2b;
    --brand-blue: #1d4a72;
    --brand-blue-deep: #00537d;
    --silver: #9a9a9a;
    --silver-light: #d6d8db;
    --paper: #f1f1f1;
    --ink-grey: #6f6f6f;
    --white: #ffffff;
  }
  * { box-sizing: border-box; margin: 0; padding: 0; }
  html, body { width: 1200px; height: 1138px; overflow: hidden; }
  body { background: var(--backdrop); position: relative; }

  .card { position: absolute; border-radius: 16px; overflow: hidden; }

  /* Front */
  .card-front {
    left: 274px; top: 185px; width: 623px; height: 377px;
    background: var(--brand-blue);
  }
  .front-firm-name {
    position: absolute; left: 0; right: 0; top: 148px;
    text-align: center;
    font-family: "Cinzel", serif; font-weight: 500;
    font-size: 27px; letter-spacing: 1px;
    color: var(--silver-light);
  }
  .front-web {
    position: absolute; left: 0; right: 0; top: 338px;
    text-align: center;
    font-family: "Noto Serif", serif; font-size: 15px;
    letter-spacing: 11px; color: var(--white);
  }

  /* Back */
  .card-back {
    left: 276px; top: 608px; width: 618px; height: 374px;
    background: var(--paper);
  }
  .back-band { position: absolute; top: 0; bottom: 0; }
  .back-band-blue { left: 0; width: 53px; background: var(--brand-blue); }
  .back-band-silver { left: 59px; width: 6px; background: var(--silver); }

  .back-firm-name {
    position: absolute; left: 86px; top: 54px;
    font-family: "Cinzel", serif; font-weight: 500;
    font-size: 24px; line-height: 27px; letter-spacing: 2px;
    color: var(--silver);
  }
  .person-name {
    position: absolute; left: 86px; top: 228px;
    font-family: "Noto Serif", serif; font-size: 28px;
    color: var(--brand-blue-deep);
  }
  .contact-list {
    position: absolute; left: 86px; top: 279px; list-style: none;
    font-family: "Noto Serif", serif; font-size: 15px; color: var(--ink-grey);
  }
  .contact-list li { display: flex; align-items: center; height: 24px; }
  .contact-icon { width: 14px; height: 14px; margin-right: 14px; fill: var(--brand-blue-deep); }
  .address {
    position: absolute; right: 32px; top: 303px; text-align: right;
    font-family: "Noto Serif", serif; font-size: 15px; line-height: 24px;
    color: var(--ink-grey);
  }
</style>
</head>
<body>

<section class="card card-front">
  <p class="front-firm-name">MOSS WHITFIELD &amp; DANBY LLP</p>
  <p class="front-web">www.mwdaccts.example</p>
</section>

<section class="card card-back">
  <div class="back-band back-band-blue"></div>
  <div class="back-band back-band-silver"></div>

  <p class="back-firm-name">Moss Whitfield<br>&amp; Danby LLP</p>

  <h1 class="person-name">Lena Whitfield</h1>

  <ul class="contact-list">
    <li>
      <svg class="contact-icon" viewBox="0 0 16 16"><path d="M1 5c0-2 3-3 7-3s7 1 7 3v1h-4V5H5v1H1z"/><rect x="3" y="7" width="10" height="7" rx="1"/></svg>
      (949)731-2864
    </li>
    <li>
      <svg class="contact-icon" viewBox="0 0 16 16"><path d="M1 3h14v10H1z M2 4l6 5 6-5" fill="none" stroke="#00537d" stroke-width="1.6"/></svg>
      www.mwdaccts.example
    </li>
    <li>
      <svg class="contact-icon" viewBox="0 0 16 16" fill="none" stroke="#00537d" stroke-width="1.4"><circle cx="8" cy="8" r="6.5"/><ellipse cx="8" cy="8" rx="2.8" ry="6.5"/><path d="M1.5 8h13M2.5 4.5h11M2.5 11.5h11"/></svg>
      lena@mwdaccts.example
    </li>
  </ul>

  <p class="address">4827 Larkspur Vale Road,<br>Irvine, CA 92614</p>
</section>

</body>
</html>
```